Therapy Services & Training

I provide counseling/therapy to individuals and families. I also travel the country and provide training at conferences.
I would like to see a card which takes my company name and design a logo using the letters "MCAC".
Target Market(s)
Therapists, non-profit organizations, clients looking for therapy
Industry/Entity Type
Training
Contact Information for Business Card
Meridel Clinical Advising & Coaching LLC
Danelle Brooks, M.S.W., LCSW
Clinical Therapist & Trainer
Providing clinical therapy services to individuals, families, couples & children. We also provide life coaching and crisis training.
helpdeskdanelle@mailbrook.example
www.meridelclinicaladvising.example
(555) 214-0397
Fairbrook, IL 60999
(BACK SIDE OF CARD)
We are certified by the Baseline Ongoing Lawyer Instruction (BOLI) Panel of the Statewide High Tribunal to provide Continuing Legal Education (CLE) credits to Illinois attorneys. Call about what courses we offer! (555) 214-0397

```html
<!DOCTYPE html>
<html lang="en">
<head>
<meta charset="utf-8">
<title>MCAC Business Card</title>
<link rel="stylesheet" href="https://fonts.googleapis.com/css2?family=Fira+Sans:wght@400;500;600&display=swap">
<style>
  :root {
    --teal: #1a9a93;
    --card-white: #f4f4f2;
    --backdrop: #ebe8e4;
    --ink-light: #ffffff;
  }
  * { box-sizing: border-box; margin: 0; padding: 0; }
  html, body {
    width: 1200px; height: 1000px; overflow: hidden;
    background: var(--backdrop);
    font-family: "Fira Sans", sans-serif;
  }
  .canvas { position: relative; width: 1200px; height: 1000px; }
  .card {
    position: absolute; width: 600px; height: 340px;
    box-shadow: 0 6px 18px rgba(0,0,0,0.12);
    overflow: hidden;
  }
  /* info side */
  .card--info { left: 60px; top: 120px; background: var(--card-white); display: flex; flex-direction: column; }
  .info-header {
    height: 82px; background: var(--teal); color: var(--ink-light);
    display: flex; justify-content: space-between; align-items: center; padding: 0 18px 0 26px;
  }
  .brand { display: flex; align-items: flex-end; gap: 8px; }
  .brand__name { font-size: 44px; font-weight: 500; letter-spacing: 1px; line-height: 1; }
  .brand__dot { width: 24px; height: 24px; border: 2px solid var(--ink-light); border-radius: 50%; margin-bottom: 2px; }
  .contact { text-align: right; font-size: 14px; line-height: 1.35; }
  .info-body {
    flex: 1; display: flex; flex-direction: column; justify-content: center;
    text-align: center; color: var(--teal); font-size: 14px; line-height: 1.38; padding: 0 16px;
  }
  .info-body p + p { margin-top: 8px; }
  .info-body .call { font-size: 20px; font-weight: 500; margin-top: 10px; }
  .info-footer {
    height: 56px; background: var(--teal); color: var(--ink-light);
    display: flex; justify-content: center; align-items: center; gap: 12px;
    font-size: 26px; font-weight: 600;
  }
  /* front side */
  .card--front {
    left: 540px; top: 570px; background: var(--teal); color: var(--ink-light);
    display: flex; flex-direction: column; align-items: center; justify-content: center;
  }
  .front-brand { display: flex; align-items: flex-end; gap: 12px; margin-left: 40px; }
  .front-brand__name { font-size: 88px; font-weight: 500; letter-spacing: 2px; line-height: 1; }
  .front-brand__dot { width: 44px; height: 44px; border: 2px solid var(--ink-light); border-radius: 50%; margin-bottom: 4px; }
  .front-company { font-size: 27px; font-weight: 500; margin-top: 14px; letter-spacing: 0.3px; }
</style>
</head>
<body>
<main class="canvas">
  <section class="card card--info">
    <header class="info-header">
      <div class="brand"><span class="brand__name">MCAC</span><span class="brand__dot"></span></div>
      <div class="contact">
        <div>helpdeskdanelle@mailbrook.example</div>
        <div>www.meridelclinicaladvising.example</div>
        <div>(555) 214-0397 Fairbrook, IL 60999</div>
      </div>
    </header>
    <div class="info-body">
      <p>Meridel Clinical Advising &amp; Coaching LLC Danelle Brooks, M.S.W.,<br>
      LCSW Clinical Therapist &amp; Trainer Providing clinical therapy services<br>
      to individuals, families, couples &amp; children.<br>
      We also provide life coaching and crisis training.</p>
      <p>We are certified by the Baseline Ongoing Lawyer Instruction (BOLI)<br>
      Panel of the Statewide High Tribunal to provide Continuing Legal Education (CLE)<br>
      credits to Illinois attorneys.</p>
      <p class="call">Call about what courses we offer!</p>
    </div>
    <footer class="info-footer">
      <svg class="phone-icon" width="16" height="28" viewBox="0 0 16 28" aria-hidden="true">
        <rect x="1" y="1" width="14" height="26" rx="2" fill="none" stroke="#fff" stroke-width="2"/>
        <rect x="4" y="4" width="8" height="8" fill="#fff"/>
        <g fill="#fff"><circle cx="5" cy="16" r="1"/><circle cx="8" cy="16" r="1"/><circle cx="11" cy="16" r="1"/>
        <circle cx="5" cy="19.5" r="1"/><circle cx="8" cy="19.5" r="1"/><circle cx="11" cy="19.5" r="1"/>
        <circle cx="5" cy="23" r="1"/><circle cx="8" cy="23" r="1"/><circle cx="11" cy="23" r="1"/></g>
      </svg>
      <span>(555) 214-0397</span>
    </footer>
  </section>

  <section class="card card--front">
    <div class="front-brand"><span class="front-brand__name">MCAC</span><span class="front-brand__dot"></span></div>
    <div class="front-company">Meridel Clinical Advising &amp; Coaching LLC</div>
  </section>
</main>
</body>
</html>
```